Veltrium stationery design

Design stationery for us that fits with the colours of the logo. We are looking for letterheads, business cards etc. Something we can use for a prospectus and marketing presentations in power point. Must be completed in such a manner that it represents a corporate image for large enterprise clients and other large organisations. The company is a project assurance and monitoring company that works in all industries.

```html
<!DOCTYPE html>
<html lang="en">
<head>
<meta charset="utf-8">
<title>Veltrium Stationery</title>
<link rel="stylesheet" href="https://fonts.googleapis.com/css2?family=Poppins:wght@600;700;800&display=swap">
<style>
  :root {
    --navy: #1a1f4d;
    --orange: #ef5d27;
    --paper: #ffffff;
    --mist: #e3e4e6;
    --sky-top: #3f6fb3;
    --sky-bottom: #0f1834;
    --night-top: #101533;
    --night-bottom: #1a2250;
    --office-top: #c7ccd3;
    --office-bottom: #3a3f4c;
  }
  html, body {
    margin: 0;
    padding: 0;
    width: 1200px;
    height: 2190px;
    overflow: hidden;
    background: var(--paper);
  }
  .board { display: block; width: 1200px; height: 2190px; }
  .brand-name {
    font-family: "Poppins", sans-serif;
    font-weight: 700;
    fill: var(--navy);
  }
  .brand-name--light { fill: var(--paper); }
  .brand-square { fill: var(--orange); }
  .fill-navy { fill: var(--navy); }
  .fill-orange { fill: var(--orange); }
  .fill-paper { fill: var(--paper); }
  .fill-mist { fill: var(--mist); }
  .eyebrow {
    font-family: "Poppins", sans-serif;
    font-weight: 700;
    font-size: 21px;
    fill: var(--paper);
  }
  .headline {
    font-family: "Poppins", sans-serif;
    font-weight: 800;
    font-size: 35px;
    fill: var(--paper);
  }
  .sheet { filter: url(#sheet-shadow); }
</style>
</head>
<body>
<svg class="board" viewBox="0 0 1050 1916" xmlns="http://www.w3.org/2000/svg">
  <defs>
    <filter id="sheet-shadow" x="-10%" y="-10%" width="125%" height="130%">
      <feDropShadow dx="6" dy="8" stdDeviation="7" flood-color="#000" flood-opacity="0.18"/>
    </filter>
    <linearGradient id="network-tone" x1="0" y1="0" x2="0" y2="1">
      <stop offset="0" stop-color="var(--night-top)"/>
      <stop offset="1" stop-color="var(--night-bottom)"/>
    </linearGradient>
    <linearGradient id="tower-tone" x1="0" y1="0" x2="1" y2="1">
      <stop offset="0" stop-color="var(--sky-top)"/>
      <stop offset="1" stop-color="var(--sky-bottom)"/>
    </linearGradient>
    <linearGradient id="meeting-tone" x1="0" y1="0" x2="0" y2="1">
      <stop offset="0" stop-color="var(--office-top)"/>
      <stop offset="1" stop-color="var(--office-bottom)"/>
    </linearGradient>
  </defs>

  <!-- Title slide -->
  <g class="slide slide--title">
    <rect class="sheet fill-paper" x="75" y="82" width="888" height="457"/>
    <polygon role="img" aria-label="Dark blue network of connected lines" fill="url(#network-tone)" points="555,82 963,82 963,539 348,539"/>
    <polygon class="fill-navy" points="75,241 240,241 127,491 75,491"/>
    <polygon class="fill-orange" points="330,185 963,185 963,435 218,435"/>
    <g class="brand">
      <rect class="brand-square" x="102" y="126" width="26" height="26"/>
      <text class="brand-name" x="138" y="150" font-size="26">VELTRIUM</text>
    </g>
    <text class="eyebrow" x="530" y="177">Our Solutions About</text>
    <text class="headline" text-anchor="middle">
      <tspan x="621" y="280">Take Control of Your</tspan>
      <tspan x="621" y="324">Projects Before They Go</tspan>
      <tspan x="621" y="368">Off Track</tspan>
    </text>
  </g>

  <!-- Content slide with towers -->
  <g class="slide slide--towers">
    <rect class="sheet fill-paper" x="75" y="570" width="427" height="220"/>
    <polygon class="fill-mist" points="75,583 325,583 247,755 75,755"/>
    <polygon class="fill-orange" points="350,570 502,570 502,744 270,744"/>
    <polygon role="img" aria-label="Glass office towers seen from below against blue sky" fill="url(#tower-tone)" points="368,593 502,593 502,744 285,744"/>
    <polygon class="fill-orange" points="75,767 303,767 280,790 75,790"/>
    <g class="brand">
      <rect class="brand-square" x="372" y="758" width="11" height="11"/>
      <text class="brand-name" x="388" y="769" font-size="12">VELTRIUM</text>
    </g>
  </g>

  <!-- Content slide with meeting -->
  <g class="slide slide--meeting">
    <rect class="sheet fill-paper" x="536" y="570" width="427" height="220"/>
    <polygon role="img" aria-label="Business colleagues in a meeting" fill="url(#meeting-tone)" points="536,570 680,570 580,790 536,790"/>
    <polygon class="fill-orange" points="680,570 703,570 603,790 580,790"/>
    <polygon class="fill-orange" points="938,570 963,570 963,575 880,740 862,740"/>
    <polygon class="fill-navy" points="963,572 963,752 880,752"/>
    <g class="brand">
      <rect class="brand-square" x="856" y="765" width="11" height="11"/>
      <text class="brand-name" x="872" y="776" font-size="12">VELTRIUM</text>
    </g>
  </g>

  <!-- Section divider slide -->
  <g class="slide slide--divider">
    <rect class="sheet fill-paper" x="75" y="820" width="427" height="220"/>
    <polygon class="fill-navy" points="75,866 345,866 345,993 323,993 303,1040 75,1040"/>
    <polygon class="fill-orange" points="355,820 502,820 502,993 275,993"/>
    <g class="brand">
      <rect class="brand-square" x="372" y="1008" width="11" height="11"/>
      <text class="brand-name" x="388" y="1019" font-size="12">VELTRIUM</text>
    </g>
  </g>

  <!-- Blank content slide -->
  <g class="slide slide--blank">
    <rect class="sheet fill-paper" x="536" y="820" width="427" height="220"/>
    <polygon class="fill-navy" points="665,832 963,832 963,855 648,855"/>
    <polygon class="fill-navy" points="536,1008 850,1008 830,1030 536,1030"/>
    <polygon class="fill-orange" points="860,1012 963,1012 963,1030 843,1030"/>
    <g class="brand">
      <rect class="brand-square" x="545" y="833" width="11" height="11"/>
      <text class="brand-name" x="561" y="844" font-size="12">VELTRIUM</text>
    </g>
  </g>

  <!-- Letterhead -->
  <g class="letterhead">
    <rect class="sheet fill-paper" x="62" y="1175" width="431" height="605"/>
    <polygon class="fill-navy" points="62,1202 250,1202 240,1216 62,1216"/>
    <polygon class="fill-orange" points="250,1203 493,1203 493,1258 203,1258"/>
    <polygon class="fill-navy" points="62,1766 250,1766 240,1780 62,1780"/>
    <polygon class="fill-orange" points="250,1768 493,1768 493,1780 243,1780"/>
    <g class="brand">
      <rect class="brand-square" x="80" y="1228" width="12" height="12"/>
      <text class="brand-name" x="98" y="1240" font-size="13">VELTRIUM</text>
    </g>
  </g>

  <!-- Business card front -->
  <g class="card card--front">
    <rect class="sheet fill-navy" x="580" y="1258" width="372" height="210"/>
    <g class="brand">
      <rect class="brand-square" x="690" y="1346" width="22" height="22"/>
      <text class="brand-name brand-name--light" x="720" y="1366" font-size="22">VELTRIUM</text>
    </g>
  </g>

  <!-- Business card back -->
  <g class="card card--back">
    <rect class="sheet fill-paper" x="580" y="1502" width="372" height="211"/>
    <polygon class="fill-navy" points="580,1502 806,1502 730,1675 580,1675"/>
    <polygon class="fill-orange" points="806,1538 740,1688 728,1713 580,1713 580,1675 730,1675"/>
    <rect class="fill-navy" x="740" y="1686" width="85" height="2.5"/>
    <rect class="fill-orange" x="828" y="1686" width="124" height="2.5"/>
    <g class="brand">
      <rect class="brand-square" x="828" y="1522" width="12" height="12"/>
      <text class="brand-name" x="846" y="1534" font-size="13">VELTRIUM</text>
    </g>
  </g>
</svg>
</body>
</html>
```